new dating app design - young, fresh, clean

Project Brief

Zivvo is the world's first dating app that actually arranges dates. The process consists of 3 easy steps:

1. use our calendar to tell us when you'd like a date
2. browse singles nearby and select who you'd like to meet
3. when your date is 1 hour away, the app will find you a nice venue in the neighborhood and send one of your matches there to meet you. All you need to do is show up and have a good time.

This design assignment consists of creating a fun, fresh & user-friendly design for the wireframes created by our UX designer. Included are 2 screens:

1. the 'calendar' screen

2. the 'matches' screen

Also included is our style guide for your reference. Feel free to use as much or as little from this guide as you please. It would be nice if we could remain somewhat consistent with our previous design (which was purely based on this style guide) but we also want you to be creative and show off your skills so by no means should you feel obliged to conform to it.

Things to consider

1. 'calendar'

this is where you tell the app when you're free for a date. You can select as many time slots as you want. The info bars at the top and the bottom are 'sticky' (will stay in place no matter where in the screen you scroll to).

Everything about this page needs to be designed: not just in terms of spacing, font and coloring of the calendar itself but also the sticky bars at the bottom and top, and the interactions (when you select a time slot, what happens visually? How will it show that this slot was selected?).

TIP: please ignore the black vs white time slot distribution you see in the image. This was meant to signify where daytime becomes nighttime and vice versa, but we're not doing that anymore. So the only difference between blocks will be the difference between a selected and an unselected block. Make sure that difference is clearly visible in your design.

2. 'matches'

this is where you tell the app whom you'd like to meet with. You can select as many people as you want by clicking their 'heart' icon. You can scroll down to see more people and again the info bars at the top and/or bottom are sticky. The design elements for this page are:

a. the page itself (sizing, spacing of the images, etc.)
b. the interactions (how does a selected heart look, how does that compare to an unselected heart)

ICONS: feel free to come up with your own iconography (ie for the 'chat' icon in the top right, and/or the 'heart' icon signifying you want to meet this person. We really like the fact that the 'matches' and 'calendar' tabs are signified with words rather than icons, but feel free to get creative on this front as well. If you can make it prettier, we're all ears :) Whatever you do on this front, make sure all your icons and the rest of your work are/is free of copyright so we can actually use them in a commercially distributed app.

The winner of this contest may get awarded a follow-up project where they will be asked to design the entire app for us.

Reason: Thank you all for your submissions. We got some promising designs but nothing that was good enough just yet. We gave some feedback for improvement and wanted to give you guys some more time to get it right. New submissions are welcome too of course. Don't hesitate to contact us if you have any questions.

Target Market(s)

singles

Industry/Entity Type

Dating

Requirements
Must have
• fresh, clean, user-friendly design of the 2 pages provided. Your design choices should include decisions about font, sizing, colours, spacing, etc.
Nice to have
• custom icons, see project brief

```html
<!DOCTYPE html>
<html lang="en">
<head>
<meta charset="utf-8">
<title>Zivvo – Matches &amp; Schedule</title>
<link rel="stylesheet" href="https://fonts.googleapis.com/css2?family=Roboto:wght@300;400;500;700&family=Delius+Swash+Caps&display=swap">
<style>
:root{
  --page:#f5f5f5;
  --screen:#ffffff;
  --coral:#f8847a;
  --peach:#f8ac68;
  --coral-text:#f07c72;
  --note-bg:#f7f7f7;
  --heart:#ef3b45;
  --white:#ffffff;
  --shadow:rgba(0,0,0,.08);
  --grad:linear-gradient(90deg,var(--coral),var(--peach));
}
*{box-sizing:border-box;margin:0;padding:0}
html,body{width:1200px;height:1200px;overflow:hidden}
body{background:var(--page);font-family:"Roboto",Arial,sans-serif;position:relative}

.screen{position:absolute;top:174px;width:480px;height:852px;background:var(--screen);overflow:hidden;box-shadow:0 4px 24px var(--shadow)}
.screen--matches{left:80px}
.screen--schedule{left:640px}

/* header */
.app-header{background:var(--grad);color:var(--white);height:158px;position:relative}
.status-bar{height:26px;display:flex;justify-content:flex-end;align-items:center;gap:7px;padding-right:12px;font-size:13px;background:rgba(0,0,0,.04)}
.status-bar svg{display:block}
.app-bar{height:62px;display:flex;align-items:center;justify-content:space-between;padding:0 20px}
.brand{display:flex;align-items:center;gap:7px;font-size:20px;font-weight:400;letter-spacing:.5px}
.brand-dot{width:10px;height:10px;border-radius:50%;background:var(--white)}
.tabs{display:flex;height:70px}
.tab{flex:1;display:flex;flex-direction:column;align-items:center;justify-content:center;gap:6px;position:relative;font-family:"Delius Swash Caps",cursive;font-size:15px;letter-spacing:2px;text-transform:uppercase}
.tab--active::after{content:"";position:absolute;left:0;right:0;bottom:0;height:3px;background:var(--white)}

/* sticky bottom bar */
.info-bar{position:absolute;left:0;right:0;bottom:0;height:70px;background:var(--grad);color:var(--white);display:flex;align-items:center;justify-content:center;text-align:center;font-size:15px;line-height:23px;letter-spacing:1px;text-transform:uppercase;font-weight:400}
.info-bar svg{vertical-align:-2px}

/* matches */
.match-grid{display:grid;grid-template-columns:205px 205px;gap:24px 26px;padding:22px 22px 0}
.match-card{background:var(--white);box-shadow:0 2px 8px var(--shadow)}
.match-photo{height:176px;position:relative;display:flex;flex-direction:column;justify-content:flex-end;padding:10px 12px;color:var(--white);font-size:14px;line-height:20px}
.match-photo .name{font-weight:700}
.match-photo .job{font-weight:300}
.photo-a{background:linear-gradient(135deg,#8a7a5e,#5a4a3c 55%,#b39a78)}
.photo-b{background:linear-gradient(135deg,#b08a56,#7a4a30 55%,#c3a070)}
.photo-c{background:linear-gradient(135deg,#e7e2dc,#c9a789 60%,#8c6a4e)}
.photo-d{background:linear-gradient(135deg,#ececec,#b7927a 55%,#4a3a34)}
.photo-e{background:linear-gradient(135deg,#6f8fb3,#5b3c2e 55%,#9fb8d4)}
.photo-f{background:linear-gradient(135deg,#dcdcdc,#3a302c 55%,#efe9e4)}
.match-like{height:50px;display:flex;align-items:center;justify-content:center}

/* schedule */
.note{background:var(--note-bg);height:64px;display:flex;align-items:center;justify-content:center;text-align:center;color:var(--coral-text);font-size:14px;line-height:21px;letter-spacing:1px;text-transform:uppercase}
.slots{padding:14px 24px 0}
.slot-row{display:grid;grid-template-columns:repeat(5,86px);height:46px;margin-bottom:20px;align-items:center}
.slot{display:flex;flex-direction:column;align-items:center;justify-content:center;color:var(--coral-text);font-size:18px;font-weight:400;line-height:20px}
.slot small{font-size:9px;letter-spacing:.5px;line-height:11px;text-transform:uppercase}
.pill{display:grid;height:46px;border-radius:23px;background:var(--grad);align-items:center;box-shadow:0 2px 6px rgba(240,124,114,.25)}
.pill .slot{color:var(--white)}
.span-3{grid-column:span 3;grid-template-columns:repeat(3,1fr)}
.span-4{grid-column:span 4;grid-template-columns:repeat(4,1fr)}
.span-5{grid-column:span 5;grid-template-columns:repeat(5,1fr)}
</style>
</head>
<body>

<!-- Matches screen -->
<section class="screen screen--matches">
  <header class="app-header">
    <div class="status-bar">
      <svg width="14" height="14" viewBox="0 0 14 14"><circle cx="7" cy="8" r="5" fill="none" stroke="#fff" stroke-width="1.5"/><path d="M7 5v3h2" stroke="#fff" stroke-width="1.3" fill="none"/></svg>
      <svg width="16" height="13" viewBox="0 0 16 13"><path d="M8 12L0 3a12 12 0 0116 0z" fill="#fff"/></svg>
      <svg width="13" height="13" viewBox="0 0 13 13"><path d="M13 0v13H0z" fill="#fff"/></svg>
      <svg width="8" height="14" viewBox="0 0 8 14"><rect x="0" y="2" width="8" height="12" rx="1" fill="#fff"/><rect x="2" y="0" width="4" height="2" fill="#fff"/></svg>
      <span>16:54</span>
    </div>
    <div class="app-bar">
      <svg width="22" height="16" viewBox="0 0 22 16"><path d="M0 1h22M0 8h22M0 15h22" stroke="#fff" stroke-width="2"/></svg>
      <div class="brand"><span class="brand-dot"></span>Zivvo</div>
      <svg width="26" height="22" viewBox="0 0 26 22"><path d="M2 2h14a2 2 0 012 2v7a2 2 0 01-2 2H8l-4 4v-4H2a2 2 0 01-2-2V4a2 2 0 012-2z" fill="#fff"/><path d="M20 6h4a2 2 0 012 2v6a2 2 0 01-2 2h-1v4l-4-4h-6a2 2 0 01-2-2v-0h5a4 4 0 004-4z" fill="#fff" opacity=".85"/></svg>
    </div>
    <nav class="tabs">
      <div class="tab tab--active">
        <svg width="20" height="18" viewBox="0 0 24 22"><path d="M12 21L2 11a6 6 0 0110-7 6 6 0 0110 7z" fill="#fff"/></svg>
        Matches
      </div>
      <div class="tab">
        <svg width="16" height="16" viewBox="0 0 16 16"><rect x="1" y="3" width="14" height="12" rx="1" fill="none" stroke="#fff" stroke-width="1.6"/><path d="M1 7h14M5 1v4M11 1v4M5 10h2M9 10h2M5 13h2M9 13h2" stroke="#fff" stroke-width="1.4"/></svg>
        Schedule
      </div>
    </nav>
  </header>

  <div class="match-grid">
    <article class="match-card">
      <div class="match-photo photo-a" role="img" aria-label="Portrait photo of Alexandra"><span><span class="name">Alexandra</span>, 24</span><span class="job">Architect</span></div>
      <div class="match-like"><svg width="20" height="18" viewBox="0 0 24 22"><path d="M12 21L2 11a6 6 0 0110-7 6 6 0 0110 7z" fill="var(--heart)"/></svg></div>
    </article>
    <article class="match-card">
      <div class="match-photo photo-b" role="img" aria-label="Portrait photo of Victoria"><span><span class="name">Victoria</span>, 26</span><span class="job">Journalism</span></div>
      <div class="match-like"><svg width="20" height="18" viewBox="0 0 24 22"><path d="M12 21L2 11a6 6 0 0110-7 6 6 0 0110 7z" fill="var(--heart)"/></svg></div>
    </article>
    <article class="match-card">
      <div class="match-photo photo-c" role="img" aria-label="Portrait photo of Olivia"><span><span class="name">Olivia</span>, 25</span><span class="job">Law Student</span></div>
      <div class="match-like"><svg width="20" height="18" viewBox="0 0 24 22"><path d="M12 21L2 11a6 6 0 0110-7 6 6 0 0110 7z" fill="var(--heart)"/></svg></div>
    </article>
    <article class="match-card">
      <div class="match-photo photo-d" role="img" aria-label="Portrait photo of Sarah"><span><span class="name">Sarah</span>, 23</span><span class="job">Engineer</span></div>
      <div class="match-like"><svg width="20" height="18" viewBox="0 0 24 22"><path d="M12 21L2 11a6 6 0 0110-7 6 6 0 0110 7z" fill="var(--heart)"/></svg></div>
    </article>
    <article class="match-card">
      <div class="match-photo photo-e" role="img" aria-label="Portrait photo of another match"></div>
    </article>
    <article class="match-card">
      <div class="match-photo photo-f" role="img" aria-label="Portrait photo of another match"></div>
    </article>
  </div>

  <footer class="info-bar">
    <p>Excellent! You can <svg width="14" height="13" viewBox="0 0 24 22"><path d="M12 21L2 11a6 6 0 0110-7 6 6 0 0110 7z" fill="#fff"/></svg> more if you'd like.<br>Next, share your schedule with us!</p>
  </footer>
</section>

<!-- Schedule screen -->
<section class="screen screen--schedule">
  <header class="app-header">
    <div class="status-bar">
      <svg width="14" height="14" viewBox="0 0 14 14"><circle cx="7" cy="8" r="5" fill="none" stroke="#fff" stroke-width="1.5"/><path d="M7 5v3h2" stroke="#fff" stroke-width="1.3" fill="none"/></svg>
      <svg width="16" height="13" viewBox="0 0 16 13"><path d="M8 12L0 3a12 12 0 0116 0z" fill="#fff"/></svg>
      <svg width="13" height="13" viewBox="0 0 13 13"><path d="M13 0v13H0z" fill="#fff"/></svg>
      <svg width="8" height="14" viewBox="0 0 8 14"><rect x="0" y="2" width="8" height="12" rx="1" fill="#fff"/><rect x="2" y="0" width="4" height="2" fill="#fff"/></svg>
      <span>16:54</span>
    </div>
    <div class="app-bar">
      <svg width="22" height="16" viewBox="0 0 22 16"><path d="M0 1h22M0 8h22M0 15h22" stroke="#fff" stroke-width="2"/></svg>
      <div class="brand"><span class="brand-dot"></span>Zivvo</div>
      <svg width="26" height="22" viewBox="0 0 26 22"><path d="M2 2h14a2 2 0 012 2v7a2 2 0 01-2 2H8l-4 4v-4H2a2 2 0 01-2-2V4a2 2 0 012-2z" fill="#fff"/><path d="M20 6h4a2 2 0 012 2v6a2 2 0 01-2 2h-1v4l-4-4h-6a2 2 0 01-2-2v-0h5a4 4 0 004-4z" fill="#fff" opacity=".85"/></svg>
    </div>
    <nav class="tabs">
      <div class="tab">
        <svg width="20" height="18" viewBox="0 0 24 22"><path d="M12 21L2 11a6 6 0 0110-7 6 6 0 0110 7z" fill="#fff"/></svg>
        Matches
      </div>
      <div class="tab tab--active">
        <svg width="16" height="16" viewBox="0 0 16 16"><rect x="1" y="3" width="14" height="12" rx="1" fill="none" stroke="#fff" stroke-width="1.6"/><path d="M1 7h14M5 1v4M11 1v4M5 10h2M9 10h2M5 13h2M9 13h2" stroke="#fff" stroke-width="1.4"/></svg>
        Schedule
      </div>
    </nav>
  </header>

  <p class="note">Choose when you're available.<br>We'll schedule your dates for you.</p>

  <div class="slots">
    <div class="slot-row">
      <span class="slot"><small>Today</small>13:00</span><span class="slot">14:00</span><span class="slot">15:00</span><span class="slot">16:00</span><span class="slot">17:00</span>
    </div>
    <div class="slot-row">
      <span class="slot">18:00</span>
      <div class="pill span-4"><span class="slot">19:00</span><span class="slot">20:00</span><span class="slot">21:00</span><span class="slot">22:00</span></div>
    </div>
    <div class="slot-row">
      <div class="pill span-5"><span class="slot">23:00</span><span class="slot"><small>Tomorrow</small>00:00</span><span class="slot">01:00</span><span class="slot">02:00</span><span class="slot">03:00</span></div>
    </div>
    <div class="slot-row">
      <div class="pill span-3"><span class="slot">04:00</span><span class="slot">05:00</span><span class="slot">06:00</span></div>
      <span class="slot">07:00</span><span class="slot">08:00</span>
    </div>
    <div class="slot-row">
      <span class="slot">09:00</span><span class="slot">10:00</span><span class="slot">11:00</span><span class="slot">12:00</span><span class="slot">13:00</span>
    </div>
    <div class="slot-row">
      <span class="slot">14:00</span><span class="slot">15:00</span><span class="slot">16:00</span><span class="slot">17:00</span><span class="slot">18:00</span>
    </div>
    <div class="slot-row">
      <div class="pill span-5"><span class="slot">19:00</span><span class="slot">20:00</span><span class="slot">21:00</span><span class="slot">23:00</span><span class="slot"><small>Friday</small>00:00</span></div>
    </div>
    <div class="slot-row">
      <div class="pill span-5"><span class="slot">01:00</span><span class="slot">02:00</span><span class="slot">03:00</span><span class="slot">04:00</span><span class="slot">05:00</span></div>
    </div>
    <div class="slot-row">
      <span class="slot">06:00</span><span class="slot">07:00</span><span class="slot">08:00</span><span class="slot">09:00</span><span class="slot">10:00</span>
    </div>
  </div>

  <footer class="info-bar">
    <p>Select the one hour block in which you're<br>available to meet up with your matches.</p>
  </footer>
</section>

</body>
</html>
```